R & M Holdings of Fairhaven, LLC
“QUALITY is the KEY to SUCCESS"
R & M Holdings of Fairhaven, LLC -
Creative Brief
Professional
Bertram Lasko
Property Manager
P.O. Box 38216 Brindlewood, XX 00000
office@holdings-mail.example

```html
<!DOCTYPE html>
<html lang="en">
<head>
<meta charset="utf-8">
<title>R &amp; M Holdings of Fairhaven, LLC — Stationery</title>
<link rel="stylesheet" href="https://fonts.googleapis.com/css2?family=Cinzel:wght@600&family=Open+Sans:wght@400;600&display=swap">
<style>
  :root{
    --board:#2e2f31;
    --board-light:#3b3c3e;
    --paper:#ffffff;
    --ink:#555555;
    --label:#bdbdbd;
    --brand-green:#8dbb3a;
    --brand-blue:#1c4fa0;
    --brand-navy:#13286b;
    --card-black:#111111;
    --faint:#e9f1dc;
  }
  *{box-sizing:border-box;margin:0;padding:0}
  html,body{width:1200px;height:314px;overflow:hidden}
  body{
    position:relative;
    background:radial-gradient(circle at 50% 45%,var(--board-light),var(--board) 75%);
    font-family:"Open Sans",Arial,sans-serif;color:var(--ink);
  }
  .piece{position:absolute;background:var(--paper);overflow:hidden;box-shadow:0 1px 4px rgba(0,0,0,.5)}
  .label{position:absolute;font-size:5px;color:var(--label);white-space:nowrap}
  .label--on-paper{color:#9a9a9a}
  .brand{font-family:"Cinzel",Georgia,serif;font-weight:600;color:var(--brand-green);white-space:nowrap;display:block}
  .mini{font-size:3.4px;line-height:1.5;color:var(--ink);white-space:nowrap}
  .corner{position:absolute;display:block}

  /* business cards */
  .section-title{position:absolute;left:72px;top:94px;font-size:5px;color:var(--label)}
  .card{width:100px;height:44px;border-radius:1px}
  .card--black{background:var(--card-black)}
  .card .brand{position:absolute;left:8px;top:8px;font-size:6px}
  .card .mini{position:absolute;left:8px;top:19px}
  .card--black .brand{left:0;right:0;top:15px;text-align:center;font-size:6px}
  .card--black .mini{left:0;right:0;top:25px;text-align:center;color:#bbb}

  /* letterheads */
  .letterhead{top:17px;width:208px;height:288px}
  .letterhead .head{position:absolute;left:12px;top:10px}
  .letterhead .head .brand{font-size:8px}
  .letterhead--centered .head{left:0;right:0;top:10px;text-align:center}
  .letterhead .watermark{position:absolute;left:0;right:0;top:112px;text-align:center;font-size:38px;color:var(--faint)}
  .letterhead .footer{position:absolute;left:0;right:0;bottom:16px;text-align:center;font-size:3.2px}
  .letterhead .label{left:0;right:0;bottom:4px;text-align:center}

  /* envelopes */
  .envelope{left:670px;width:236px;border-radius:14px 2px 14px 2px}
  .envelope .head{position:absolute;left:14px;top:12px}
  .envelope .brand{font-size:7px}
  .envelope .mini{margin-top:2px}
  .envelope .watermark{position:absolute;left:0;right:0;top:34px;text-align:center;font-size:26px;color:var(--faint)}
  .envelope .label{right:30px;bottom:4px}

  .envelope-back{left:924px;width:252px}
  .envelope-back svg{position:absolute;inset:0}
  .envelope-back .center{position:absolute;left:0;right:0;top:38px;text-align:center}
  .envelope-back .center .brand{font-size:12px}
</style>
</head>
<body>

<svg width="0" height="0" style="position:absolute" aria-hidden="true">
  <defs>
    <linearGradient id="swoosh-grad" x1="0" y1="0" x2="1" y2="1">
      <stop offset="0" stop-color="#8dbb3a"/>
      <stop offset=".45" stop-color="#1c4fa0"/>
      <stop offset="1" stop-color="#13286b"/>
    </linearGradient>
    <linearGradient id="band-blue" x1="0" y1="0" x2="1" y2="1">
      <stop offset="0" stop-color="#1f5fb8"/>
      <stop offset=".6" stop-color="#1c4fa0"/>
      <stop offset="1" stop-color="#0f2466"/>
    </linearGradient>
    <linearGradient id="band-gold" x1="0" x2="1">
      <stop offset="0" stop-color="#b9800f"/>
      <stop offset=".5" stop-color="#f1c24a"/>
      <stop offset="1" stop-color="#b9800f"/>
    </linearGradient>
  </defs>
</svg>

<p class="section-title">Creative Brief</p>

<!-- Business cards -->
<div class="piece card" style="left:19px;top:112px">
  <span class="brand">R &amp; M</span>
  <p class="mini">Bertram Lasko<br>Property Manager</p>
</div>
<div class="piece card card--black" style="left:70px;top:112px;left:124px">
  <span class="brand">R &amp; M</span>
</div>
<p class="label" style="left:30px;top:159px">Business Card Front</p>
<p class="label" style="left:136px;top:159px">Business Card Back</p>

<div class="piece card" style="left:19px;top:173px">
  <span class="brand">R &amp; M</span>
  <p class="mini">P.O. Box 38216 Brindlewood, XX 00000<br>office@holdings-mail.example</p>
</div>
<div class="piece card card--black" style="left:124px;top:173px">
  <span class="brand">R &amp; M</span>
  <p class="mini">“QUALITY is the KEY to SUCCESS"</p>
</div>
<p class="label" style="left:30px;top:220px">Business Card Front</p>
<p class="label" style="left:136px;top:220px">Business Card Back</p>

<!-- Letterhead 1 -->
<div class="piece letterhead" style="left:223px">
  <svg class="corner" style="right:0;top:0" width="14" height="22" viewBox="0 0 14 22" aria-hidden="true"><path d="M0 0 H14 V22 Q12 6 0 0 Z" fill="url(#swoosh-grad)"/></svg>
  <div class="head">
    <span class="brand">R &amp; M</span>
    <p class="mini">R &amp; M Holdings of Fairhaven, LLC</p>
  </div>
  <div class="watermark brand">R &amp; M</div>
  <svg class="corner" style="left:0;bottom:0" width="14" height="22" viewBox="0 0 14 22" aria-hidden="true"><path d="M14 22 H0 V0 Q2 16 14 22 Z" fill="url(#swoosh-grad)"/></svg>
  <p class="label label--on-paper">Letterhead Sheet 1</p>
</div>

<!-- Letterhead 2 -->
<div class="piece letterhead letterhead--centered" style="left:449px">
  <svg class="corner" style="right:0;top:0" width="14" height="22" viewBox="0 0 14 22" aria-hidden="true"><path d="M0 0 H14 V22 Q12 6 0 0 Z" fill="url(#swoosh-grad)"/></svg>
  <div class="head"><span class="brand">R &amp; M</span></div>
  <div class="watermark brand">R &amp; M</div>
  <p class="footer">P.O. Box 38216 Brindlewood, XX 00000 · office@holdings-mail.example</p>
  <svg class="corner" style="left:0;bottom:0" width="14" height="22" viewBox="0 0 14 22" aria-hidden="true"><path d="M14 22 H0 V0 Q2 16 14 22 Z" fill="url(#swoosh-grad)"/></svg>
  <p class="label label--on-paper">Letterhead Sheet 2</p>
</div>

<!-- Envelope fronts -->
<div class="piece envelope" style="top:48px;height:100px">
  <div class="head">
    <span class="brand">R &amp; M</span>
    <p class="mini">R &amp; M Holdings of Fairhaven, LLC</p>
  </div>
  <p class="label label--on-paper">Envelope Front A</p>
</div>

<div class="piece envelope" style="top:164px;height:104px">
  <div class="head">
    <span class="brand">R &amp; M</span>
    <p class="mini">P.O. Box 38216 Brindlewood, XX 00000</p>
  </div>
  <div class="watermark brand">R &amp; M</div>
  <p class="label label--on-paper">Envelope Front B</p>
</div>

<!-- Envelope flap options -->
<div class="piece envelope-back" style="top:31px;height:66px">
  <svg viewBox="0 0 252 66" width="252" height="66" preserveAspectRatio="none" aria-hidden="true"><path d="M0 0 H252 V50 Q126 80 0 50 Z" fill="url(#band-blue)"/></svg>
</div>
<div class="piece envelope-back" style="top:103px;height:58px">
  <svg viewBox="0 0 252 58" width="252" height="58" preserveAspectRatio="none" aria-hidden="true"><path d="M0 0 H252 V40 Q126 70 0 40 Z" fill="url(#band-gold)"/></svg>
</div>
<div class="piece envelope-back" style="top:168px;height:96px">
  <svg viewBox="0 0 252 96" width="252" height="96" preserveAspectRatio="none" aria-hidden="true"><path d="M0 8 Q126 50 252 8" fill="none" stroke="#dddddd" stroke-width="1"/></svg>
  <div class="center">
    <span class="brand">R &amp; M</span>
    <p class="mini">R &amp; M Holdings of Fairhaven, LL</p>
  </div>
</div>
<p class="label" style="left:1010px;top:269px">Envelope Flap Options</p>

</body>
</html>
```